Quarlwick Builders Business Cards

I want to use the logo and make an unique business card that shows the textured Logo with brick and builings. I want to be able to stand out when I pass out business cards.

```html
<!DOCTYPE html>
<html lang="en">
<head>
<meta charset="utf-8">
<title>Quarlwick Builders Business Cards</title>
<link href="https://fonts.googleapis.com/css2?family=Montserrat:wght@400;500;600;700;800&display=swap" rel="stylesheet">
<style>
  :root {
    --backdrop: #2b2f36;
    --concrete-light: #8d8c88;
    --concrete-mid: #6f6e6a;
    --concrete-dark: #4c4b48;
    --brick: #d9462a;
    --brick-deep: #a8301c;
    --ink-white: #ffffff;
    --ink-grey: #8a8a8a;
    --tag-blue: #2b4f8f;
    --logo-red: #c9472b;
  }
  * { margin: 0; padding: 0; box-sizing: border-box; }
  html, body { width: 1200px; height: 848px; overflow: hidden; }
  body {
    background: var(--backdrop);
    font-family: "Montserrat", sans-serif;
    display: flex;
    align-items: center;
    justify-content: center;
    gap: 30px;
  }
  .card {
    position: relative;
    width: 560px;
    height: 320px;
    border-radius: 6px;
    overflow: hidden;
    box-shadow: 0 14px 30px rgba(0,0,0,0.45);
  }
  .card-front {
    background: linear-gradient(135deg, var(--concrete-mid) 0%, var(--concrete-light) 55%, #9a9995 100%);
  }
  .watermark-name {
    position: absolute;
    left: 270px;
    top: 100px;
    font-weight: 800;
    font-size: 38px;
    line-height: 1;
    color: var(--logo-red);
    opacity: 0.22;
    width: 260px;
  }
  .brick-wall {
    position: absolute;
    inset: 0;
    width: 560px;
    height: 320px;
  }
  .holder-name {
    position: absolute;
    left: 34px;
    top: 108px;
    font-weight: 700;
    font-size: 28px;
    color: var(--ink-white);
  }
  .designation {
    position: absolute;
    left: 34px;
    top: 148px;
    width: 190px;
    height: 24px;
    background: var(--ink-white);
    clip-path: polygon(0 0, 100% 0, 90% 100%, 0 100%);
    font-size: 12.5px;
    font-weight: 500;
    color: var(--ink-grey);
    padding: 4px 10px;
  }
  .contact-list {
    position: absolute;
    left: 34px;
    top: 200px;
    list-style: none;
    color: var(--ink-white);
    font-size: 14px;
    font-weight: 500;
  }
  .contact-list li {
    display: flex;
    align-items: flex-start;
    gap: 10px;
    line-height: 20px;
    margin-bottom: 2px;
  }
  .contact-list svg { width: 14px; height: 14px; margin-top: 3px; flex: none; }
  .card-back {
    background: radial-gradient(ellipse at 50% 45%, #a3a29e 0%, var(--concrete-mid) 55%, var(--concrete-dark) 100%);
    display: flex;
    flex-direction: column;
    align-items: center;
    justify-content: center;
    gap: 10px;
  }
  .brand-name {
    font-weight: 800;
    font-size: 36px;
    color: var(--logo-red);
    letter-spacing: 0.5px;
  }
  .services {
    font-weight: 700;
    font-size: 11px;
    color: var(--tag-blue);
  }
</style>
</head>
<body>
  <section class="card card-front">
    <div class="watermark-name">Quarlwick Builders</div>
    <svg class="brick-wall" viewBox="0 0 560 320" role="img" aria-label="Stepped red brick wall rising to the top right">
      <defs>
        <linearGradient id="brickTone" x1="0" y1="0" x2="1" y2="1">
          <stop offset="0" stop-color="var(--brick)"/>
          <stop offset="1" stop-color="var(--brick-deep)"/>
        </linearGradient>
      </defs>
      <polygon fill="url(#brickTone)" points="560,40 450,40 450,70 428,70 428,100 406,100 406,130 384,130 384,160 362,160 362,190 340,190 340,220 318,220 318,250 296,250 296,285 274,285 274,320 560,320"/>
    </svg>
    <h1 class="holder-name">John Smith</h1>
    <div class="designation">Designation Here</div>
    <ul class="contact-list">
      <li>
        <svg viewBox="0 0 14 14"><circle cx="7" cy="7" r="7" fill="#fff"/><path d="M7 3a2.5 2.5 0 0 0-2.5 2.5C4.5 7.5 7 10.5 7 10.5s2.5-3 2.5-5A2.5 2.5 0 0 0 7 3z" fill="#777"/></svg>
        <span>Your Address goes here,<br>Your city</span>
      </li>
      <li>
        <svg viewBox="0 0 14 14"><circle cx="7" cy="7" r="7" fill="#fff"/><path d="M4.5 3.5l1.5 0 .7 2-1 .8a5 5 0 0 0 2.5 2.5l.8-1 2 .7v1.5a1 1 0 0 1-1 1A6.5 6.5 0 0 1 3.5 4.5a1 1 0 0 1 1-1z" fill="#777"/></svg>
        <span>0123 654 987</span>
      </li>
      <li>
        <svg viewBox="0 0 14 14"><circle cx="7" cy="7" r="7" fill="#fff"/><rect x="3.5" y="4.5" width="7" height="5" rx="0.6" fill="#777"/><path d="M3.8 4.8L7 7.3l3.2-2.5" stroke="#fff" stroke-width="0.8" fill="none"/></svg>
        <span>Your@email.com</span>
      </li>
      <li>
        <svg viewBox="0 0 14 14"><circle cx="7" cy="7" r="7" fill="#fff"/><circle cx="7" cy="7" r="3.6" fill="none" stroke="#777" stroke-width="0.9"/><path d="M3.4 7h7.2M7 3.4c-1.6 2-1.6 5.2 0 7.2M7 3.4c1.6 2 1.6 5.2 0 7.2" stroke="#777" stroke-width="0.8" fill="none"/></svg>
        <span>www.QuarlwickBuilders.com</span>
      </li>
    </ul>
  </section>

  <section class="card card-back">
    <div class="brand-name">Quarlwick Builders</div>
    <div class="services">Patios - Sidewalks - Retaining Walls - Foundations</div>
  </section>
</body>
</html>
```